Weather card for guests at Marlow’s Beach House

I am looking to have a card designed for my guests who stay over. The card should show the weather for the next day (emoji's), quote of the day, Activities of the day. It's for a beach house so it should be coastal/Beachy themed. The weather should have a high and a low. (I will fill in each card). It should be front and back. It should be a fun project. Think modern farmhouse. The top of each card should say something like Another great Day at 7 Harbor
Updates

If you google "turn down Service letter" or "hotel weather card". It will provide examples

Target Market(s)

Our guests who visit our beach house

Font styles to use
Sans Serif

Colors
0054AA
0677BA
7BADD7
CADEEF
E8F1F8

Requirements
Must have
• weather options, quote of the day, activity for the day
Nice to have
• Sand, seashells, seagulls
Should not have
• Should not be too busy and not childish

```html
<!DOCTYPE html>
<html lang="en">
<head>
<meta charset="utf-8">
<title>Weather Card – 7 Harbor</title>
<link href="https://fonts.googleapis.com/css2?family=Bebas+Neue&family=Great+Vibes&family=Playfair+Display:ital,wght@0,400;0,700;1,400;1,700&family=Poppins:wght@300;400;600&display=swap" rel="stylesheet">
<style>
  :root{
    --board:#cad5ee;
    --label-red:#e8262a;
    --cream:#f8f2dc;
    --ink-brown:#7a5f55;
    --ink-grey:#6d6461;
    --ink-dark:#2f2a28;
    --quote-orange:#f08a3c;
    --sun:#f9b90a;
    --cloud:#1aa9d6;
    --box-line:#b9b0a6;
    --teal:#00a9ad;
    --sand:#f7c98b;
    --ocean-deep:#0a5fae;
    --ocean-mid:#1a8fd0;
    --ocean-light:#3cc3dc;
    --logo-tint:#a9e4e6;
    --contact-label:#f6d77a;
    --contact-text:#e9f6f6;
  }
  *{box-sizing:border-box;margin:0;padding:0}
  html,body{width:1200px;height:1200px;overflow:hidden;background:var(--board)}
  .board{position:relative;width:1200px;height:1200px}
  .spec-label{position:absolute;left:184px;top:30px;font:600 21px/1.4 "Poppins",sans-serif;color:var(--label-red);letter-spacing:1.2px}

  .card{position:absolute;width:787px;height:491px;overflow:hidden;box-shadow:0 8px 18px rgba(40,50,80,.35)}
  .card--front{left:174px;top:114px;background:var(--cream)}
  .card--back{left:182px;top:675px}

  .shore{position:absolute;left:0;bottom:0;width:100%;height:150px}
  .front-content{position:absolute;inset:0;text-align:center}
  .greeting{position:absolute;top:18px;width:100%;font:400 18px/1.2 "Playfair Display",serif;color:var(--ink-grey);letter-spacing:-.3px}
  .greeting .place{font-size:29px;margin-left:6px}
  .quote{position:absolute;top:58px;width:100%;font:400 50px/1.2 "Great Vibes",cursive;color:var(--quote-orange);padding-left:40px;letter-spacing:.5px}
  .section-title{position:absolute;width:100%;font:400 18px/1 "Bebas Neue",sans-serif;color:var(--ink-brown);letter-spacing:.5px}
  .section-title--forecast{top:143px}
  .section-title--temp{top:274px}
  .section-title--activities{top:355px}

  .forecast{position:absolute;top:172px;left:0;width:100%}
  .forecast-option{position:absolute;width:80px;margin-left:-40px;text-align:center}
  .forecast-option svg{display:block;margin:0 auto;width:60px;height:56px}
  .check-box{display:block;width:20px;height:20px;border:1px solid var(--box-line);margin:9px auto 0}

  .temps{position:absolute;top:307px;left:0;width:100%;font:400 11px/1 "Poppins",sans-serif;color:var(--ink-grey)}
  .temp{position:absolute}
  .temp .fill-line{display:inline-block;width:62px;border-bottom:1px solid var(--box-line);margin-left:5px;vertical-align:-1px}
  .temp--high{left:278px}
  .temp--low{left:426px}

  .activities{position:absolute;top:387px;width:100%;font:400 13px/1.3 "Playfair Display",serif;color:var(--ink-dark);letter-spacing:-.2px;padding-left:10px}

  .back-art{position:absolute;inset:0;width:100%;height:100%}
  .brand{position:absolute;left:36px;top:382px;font:300 46px/1 "Poppins",sans-serif;color:var(--logo-tint);display:flex;flex-direction:column;align-items:center}
  .brand span{display:block}
  .brand .brand-sub{font-size:16px;font-weight:400;margin-top:12px;letter-spacing:.4px}
  .contact{position:absolute;left:571px;top:404px;font:400 12.5px/16.5px "Playfair Display",serif;color:var(--contact-text);list-style:none}
  .contact b{font-style:italic;font-weight:700;color:var(--contact-label);display:inline-block;width:19px}
</style>
</head>
<body>
<main class="board">
  <p class="spec-label">Weathrer Card, Size: 8in(width) X 5 iN(height),&nbsp; Color Mode: CMYK</p>

  <section class="card card--front" aria-label="Weather card front">
    <svg class="shore" viewBox="0 0 787 150" preserveAspectRatio="none" role="img" aria-label="Sea foam and shallow waves washing onto the sand">
      <defs>
        <linearGradient id="shoreFade" x1="0" y1="0" x2="0" y2="1">
          <stop offset="0" stop-color="#f8f2dc" stop-opacity="0"/>
          <stop offset=".35" stop-color="#ffffff" stop-opacity=".85"/>
          <stop offset=".7" stop-color="#e9f7fa"/>
          <stop offset="1" stop-color="#45bfd6"/>
        </linearGradient>
      </defs>
      <path d="M0 30 C80 10 150 40 230 20 C300 5 360 35 440 30 C520 25 560 0 640 15 C700 25 740 30 787 20 L787 150 L0 150 Z" fill="url(#shoreFade)"/>
    </svg>

    <div class="front-content">
      <h1 class="greeting">Another Great Day At <span class="place">7 Harbor</span></h1>
      <p class="quote">An ocean breeze puts a mind at ease</p>

      <h2 class="section-title section-title--forecast">Tomorrow's Weather Forecast</h2>
      <div class="forecast">
        <div class="forecast-option" style="left:217px">
          <svg viewBox="0 0 60 56" aria-label="Sunny" fill="none" stroke="var(--sun)" stroke-width="2.5" stroke-linecap="round">
            <circle cx="30" cy="28" r="10"/>
            <path d="M30 8v6M30 42v6M10 28h6M44 28h6M16 14l4 4M40 38l4 4M44 14l-4 4M20 38l-4 4"/>
          </svg>
          <span class="check-box"></span>
        </div>
        <div class="forecast-option" style="left:332px">
          <svg viewBox="0 0 60 56" aria-label="Partly cloudy" fill="none" stroke-width="2.5" stroke-linecap="round" stroke-linejoin="round">
            <g stroke="var(--sun)">
              <path d="M14 26a9 9 0 0 1 16-8"/>
              <path d="M22 6v4M8 12l3 3M4 26h4M36 12l-3 3"/>
            </g>
            <path d="M16 46h30a8 8 0 0 0 0-16 12 12 0 0 0-23 3 7 7 0 0 0-7 13z" stroke="var(--cloud)"/>
          </svg>
          <span class="check-box"></span>
        </div>
        <div class="forecast-option" style="left:446px">
          <svg viewBox="0 0 60 56" aria-label="Cloudy" fill="none" stroke="var(--cloud)" stroke-width="2.5" stroke-linecap="round" stroke-linejoin="round">
            <path d="M12 42h34a9 9 0 0 0 0-18 14 14 0 0 0-26 4 7 7 0 0 0-8 14z"/>
          </svg>
          <span class="check-box"></span>
        </div>
        <div class="forecast-option" style="left:560px">
          <svg viewBox="0 0 60 56" aria-label="Rain" fill="none" stroke="var(--cloud)" stroke-width="2.5" stroke-linecap="round" stroke-linejoin="round">
            <path d="M12 34h34a9 9 0 0 0 0-18 14 14 0 0 0-26 4 7 7 0 0 0-8 14z"/>
            <path d="M20 40l-3 8M30 40l-3 8M40 40l-3 8"/>
          </svg>
          <span class="check-box"></span>
        </div>
      </div>

      <h2 class="section-title section-title--temp">Temperature</h2>
      <div class="temps">
        <span class="temp temp--high">High<span class="fill-line"></span></span>
        <span class="temp temp--low">Low<span class="fill-line"></span></span>
      </div>

      <h2 class="section-title section-title--activities">Activities of the Day</h2>
      <p class="activities">Start your day with breakfast at 7 Harbor.<br>It was my pleasure to prepare your suite for a restful night.</p>
    </div>
  </section>

  <section class="card card--back" aria-label="Weather card back">
    <svg class="back-art" viewBox="0 0 787 491" preserveAspectRatio="none">
      <defs>
        <linearGradient id="oceanTone" x1="0" y1="0" x2="0.3" y2="1">
          <stop offset="0" stop-color="var(--ocean-deep)"/>
          <stop offset=".45" stop-color="var(--ocean-mid)"/>
          <stop offset=".75" stop-color="var(--ocean-light)"/>
          <stop offset="1" stop-color="#8fcf6a"/>
        </linearGradient>
      </defs>
      <rect width="787" height="400" fill="url(#oceanTone)" role="img" aria-label="Aerial photo of a turquoise bay with a floating water park and a tree-lined beach"/>
      <path d="M0 216 C220 340 470 385 700 330 L787 491 L0 491 Z" fill="var(--sand)"/>
      <path d="M340 378 C540 365 700 300 787 238 L787 491 L340 491 Z" fill="#ffffff"/>
      <path d="M0 275 C200 380 470 400 600 370 C690 345 750 300 787 263 L787 491 L0 491 Z" fill="var(--teal)"/>
    </svg>

    <div class="brand"><span>7 Harbor</span><span class="brand-sub">Beach House</span></div>

    <ul class="contact">
      <li><b>P:</b> 555 0142 7820</li>
      <li><b>R:</b> 555 0193 44</li>
      <li><b>E:</b> info@7harborbeachhouse.com</li>
      <li><b>W:</b> www.7harborbeachhouse.com</li>
    </ul>
  </section>
</main>
</body>
</html>
```